Graphics for Book geared to Professionals

We need the attached graphics professional recreated for our book. The book will be in black and white so it will need to be grey scale. Please see the best practices for graphics from our publisher Harlow.
The power point attached has several graphics that we need professional illustrated. The graphics in a excel format simply need to be transposed professionally (slides 8-14). The graphs in the other slides need to have some design put behind them. These make the general look and feel somewhat consistent. If you have any questions, you can email me at martin.hobbs@quorvex.com.

Target Market(s)

Professionals, Business Analyst

Industry/Entity Type

It Professional

Font styles to use
Other font styles liked:
• Calibre

Requirements
Must have
• Professional looks and feel

```html
<!DOCTYPE html>
<html lang="en">
<head>
<meta charset="utf-8">
<title>Poison Ivy Treatment Workflow</title>
<link rel="stylesheet" href="https://fonts.googleapis.com/css2?family=Raleway:wght@400;500;600;700&display=swap">
<style>
  :root {
    --ink: #333333;
    --ink-strong: #222222;
    --rule: #d9d9d9;
    --divider: #bdbdbd;
    --mark: #4a4a4a;
    --plant-light: #eeeeee;
    --plant-mid: #dcdcdc;
    --bg: #ffffff;
  }
  * { margin: 0; padding: 0; box-sizing: border-box; }
  html, body { width: 1200px; height: 715px; overflow: hidden; background: var(--bg); }
  .workflow {
    position: relative; width: 1200px; height: 715px;
    font-family: "Raleway", sans-serif; color: var(--ink); font-size: 17px;
  }
  .txt { position: absolute; white-space: nowrap; line-height: 1; transform: translateY(-50%); }
  .column-head { font-weight: 700; font-size: 20px; color: var(--ink-strong); }
  .column-rule { position: absolute; height: 2px; background: linear-gradient(90deg, var(--mark), rgba(74,74,74,0)); }
  .stage-label { font-weight: 700; font-size: 21px; color: var(--ink-strong); }
  .stage-icon { position: absolute; }
  .section-divider { position: absolute; left: 30px; width: 1105px; height: 1px; background: var(--rule); }
  .column-divider { position: absolute; width: 1px; background: var(--divider); }
  .note { font-size: 16px; color: #555; }
  .diagnostic-art {
    position: absolute; left: 838px; top: 252px; width: 118px; height: 156px;
    background: radial-gradient(ellipse at 50% 40%, var(--plant-mid), var(--plant-light) 60%, rgba(255,255,255,0) 75%);
  }
  .diagnostic-title {
    position: absolute; left: 800px; top: 305px; width: 120px;
    text-align: center; font-weight: 700; font-size: 17px; line-height: 22px; color: var(--ink-strong);
  }
  .step-mark { position: absolute; }
</style>
</head>
<body>
<main class="workflow">

  <span class="txt column-head" style="left:267px; top:25px;">Doctor</span>
  <div class="column-rule" style="left:265px; top:38px; width:110px;"></div>
  <span class="txt column-head" style="left:600px; top:23px;">Patient</span>
  <div class="column-rule" style="left:598px; top:38px; width:110px;"></div>

  <!-- Inform -->
  <svg class="stage-icon" style="left:42px; top:125px;" width="38" height="40" viewBox="0 0 38 40" aria-hidden="true">
    <rect x="2" y="5" width="24" height="32" fill="#8a8a8a" stroke="#333" stroke-width="1.5"/>
    <rect x="5" y="2" width="18" height="5" fill="#333"/>
    <path d="M16 28 L30 8 L34 11 L20 31 L15 33 Z" fill="#fff" stroke="#333" stroke-width="1.5"/>
    <rect x="18" y="28" width="9" height="9" fill="#fff" stroke="#333" stroke-width="1.5"/>
  </svg>
  <span class="txt stage-label" style="left:117px; top:145px;">Inform</span>
  <div class="column-divider" style="left:236px; top:55px; height:184px;"></div>
  <div class="column-divider" style="left:571px; top:55px; height:184px;"></div>

  <span class="txt" style="left:267px; top:64px;">What are the patients vitals?</span>
  <span class="txt" style="left:267px; top:105px;">What seems to be the problem?</span>
  <span class="txt" style="left:267px; top:147px;">How long have you had the rash?</span>
  <span class="txt" style="left:267px; top:188px;">Where is the rash located?</span>
  <span class="txt" style="left:267px; top:230px;">Where did you get the rash?</span>

  <span class="txt" style="left:600px; top:64px;">Blood pressure, heart rate, weight all look normal</span>
  <span class="txt" style="left:600px; top:105px;">I have a rash</span>
  <span class="txt" style="left:600px; top:147px;">2 days</span>
  <span class="txt" style="left:600px; top:185px;">On my forearm</span>
  <span class="txt" style="left:600px; top:226px;">In my garden</span>

  <svg style="position:absolute; left:758px; top:200px;" width="52" height="44" viewBox="0 0 52 44" aria-hidden="true">
    <path d="M2 34 Q20 28 32 32" fill="none" stroke="var(--mark)" stroke-width="3" stroke-linecap="round"/>
    <path d="M28 4 Q44 20 46 42 Q40 22 26 8 Z" fill="var(--mark)"/>
  </svg>
  <span class="txt note" style="left:820px; top:195px;">Determines issue is probably associated</span>
  <span class="txt note" style="left:834px; top:217px;">with a poisonous plant</span>

  <div class="section-divider" style="top:248px;"></div>

  <!-- Diagnose -->
  <svg class="stage-icon" style="left:44px; top:306px;" width="36" height="54" viewBox="0 0 36 54" aria-hidden="true">
    <path d="M6 2 V18 Q6 30 16 30 Q26 30 26 18 V2" fill="none" stroke="#333" stroke-width="2"/>
    <path d="M16 30 V44 Q16 52 22 52 Q28 52 28 44 V38" fill="none" stroke="#333" stroke-width="2"/>
    <circle cx="28" cy="34" r="4" fill="none" stroke="#333" stroke-width="2"/>
  </svg>
  <span class="txt stage-label" style="left:117px; top:332px;">Diagnose</span>
  <div class="column-divider" style="left:236px; top:260px; height:146px;"></div>
  <div class="column-divider" style="left:571px; top:260px; height:146px;"></div>

  <span class="txt" style="left:267px; top:271px;">Lets look at the Rash?</span>
  <span class="txt" style="left:267px; top:313px;">Are there blisters?</span>
  <span class="txt" style="left:267px; top:354px;">Are rash &amp; blisters severe?</span>
  <span class="txt" style="left:267px; top:392px;">DECISION: What should I treat for?</span>

  <span class="txt" style="left:600px; top:268px;">Small red spots</span>
  <span class="txt" style="left:600px; top:309px;">Yes</span>
  <span class="txt" style="left:600px; top:350px;">Yes</span>
  <span class="txt" style="left:600px; top:391px;">Poison Ivy</span>

  <svg style="position:absolute; left:740px; top:258px;" width="70" height="152" viewBox="0 0 70 152" aria-hidden="true">
    <path d="M8 6 Q48 76 8 148 Q32 76 8 6 Z" fill="var(--mark)"/>
    <path d="M52 68 L60 82 L52 96 Z" fill="var(--mark)"/>
  </svg>
  <div class="diagnostic-art" role="img" aria-label="Light grey illustration of a poisonous plant with hazard-marked leaves"></div>
  <div class="diagnostic-title">Poisonous<br>Plant<br>Diagnostic</div>

  <div class="section-divider" style="top:416px;"></div>

  <!-- Action -->
  <svg class="stage-icon" style="left:30px; top:460px;" width="64" height="48" viewBox="0 0 64 48" aria-hidden="true">
    <rect x="18" y="4" width="22" height="14" rx="2" transform="rotate(40 29 11)" fill="#333"/>
    <rect x="30" y="18" width="26" height="6" transform="rotate(40 30 21)" fill="#333"/>
    <rect x="2" y="42" width="30" height="4" fill="#333"/>
    <rect x="8" y="36" width="18" height="5" fill="#333"/>
  </svg>
  <span class="txt stage-label" style="left:117px; top:483px;">Action</span>
  <div class="column-divider" style="left:236px; top:430px; height:114px;"></div>

  <svg class="step-mark" style="left:268px; top:440px;" width="16" height="14" viewBox="0 0 16 14" aria-hidden="true"><path d="M1 13 Q8 4 15 1 Q10 8 9 13 Z" fill="#777"/></svg>
  <span class="txt" style="left:303px; top:446px;">Prescribe a Topical Steroid, call Pharmacist Explain Treatment to patient</span>
  <svg class="step-mark" style="left:268px; top:481px;" width="16" height="14" viewBox="0 0 16 14" aria-hidden="true"><path d="M1 13 Q8 4 15 1 Q10 8 9 13 Z" fill="#777"/></svg>
  <span class="txt" style="left:303px; top:487px;">Recommend OTC pain medication if itching is bad</span>
  <svg class="step-mark" style="left:268px; top:522px;" width="16" height="14" viewBox="0 0 16 14" aria-hidden="true"><path d="M1 13 Q8 4 15 1 Q10 8 9 13 Z" fill="#777"/></svg>
  <span class="txt" style="left:303px; top:528px;">Patient follows Doctors instructions for prescribed duration of treatment plan</span>

  <div class="section-divider" style="top:562px;"></div>

  <!-- Measure -->
  <svg class="stage-icon" style="left:36px; top:608px;" width="52" height="40" viewBox="0 0 52 40" aria-hidden="true">
    <path d="M2 38 V4 L36 38 Z" fill="none" stroke="#777" stroke-width="4"/>
    <path d="M10 32 A16 16 0 0 1 42 32 Z" fill="none" stroke="#222" stroke-width="4"/>
  </svg>
  <span class="txt stage-label" style="left:117px; top:628px;">Measure</span>
  <div class="column-divider" style="left:236px; top:575px; height:114px;"></div>

  <svg class="step-mark" style="left:268px; top:587px;" width="16" height="14" viewBox="0 0 16 14" aria-hidden="true"><path d="M1 13 Q8 4 15 1 Q10 8 9 13 Z" fill="#777"/></svg>
  <span class="txt" style="left:303px; top:593px;">Patient to visually inspect rash and blisters, should see signs of improvement in 2-3 days</span>
  <svg class="step-mark" style="left:268px; top:629px;" width="16" height="14" viewBox="0 0 16 14" aria-hidden="true"><path d="M1 13 Q8 4 15 1 Q10 8 9 13 Z" fill="#777"/></svg>
  <span class="txt" style="left:303px; top:635px;">If rash improves, no follow up needed</span>
  <svg class="step-mark" style="left:268px; top:670px;" width="16" height="14" viewBox="0 0 16 14" aria-hidden="true"><path d="M1 13 Q8 4 15 1 Q10 8 9 13 Z" fill="#777"/></svg>
  <span class="txt" style="left:303px; top:676px;">If no improvement within 5 days, call Doctor for a follow up visit, may need a more aggressive treatment</span>

</main>
</body>
</html>
```